Business Card for Makeup Artist

I need a business card designed for my makeup and hair artistry business which is primarily events and weddings focused. The card needs to be sleek, simple, stylish and appealing to women. I would prefer a white background but open to suggestions also. I also love the marble background look. I have attached some example pics. It needs to be a double sided card with logo and/or design on one side and contact details in the centre of the card on the other side. NO LOGO ON BACK. Examples attached.

Target Market(s)

Females age 14-55

Industry/Entity Type

Business

Contact Information for Business Card

Nora Vint
Principal Makeup Artist
P: 0413 925 214
E: nora@lumirabeauty.com.au
W: www.lumirabeauty.com.au

Requirements
Should not have
• No yellow, green, red or blue in the design.

```html
<!DOCTYPE html>
<html lang="en">
<head>
<meta charset="utf-8">
<title>Lumira Makeup Artistry – Business Card</title>
<link href="https://fonts.googleapis.com/css2?family=Lato:wght@400;700&display=swap" rel="stylesheet">
<style>
  :root {
    --page: #e4e4e4;
    --black: #141414;
    --black-soft: #2a2a2a;
    --gold: #c9a24a;
    --gold-light: #e2c47a;
    --white: #ffffff;
    --band: #eeeeee;
    --text-light: #f1f1f1;
  }
  * { margin: 0; padding: 0; box-sizing: border-box; }
  html, body { width: 1200px; height: 1200px; overflow: hidden; }
  body {
    background: var(--page);
    font-family: "Lato", Arial, sans-serif;
    position: relative;
  }
  .card {
    position: absolute;
    left: 150px;
    width: 900px;
    height: 514px;
    background: var(--white);
    overflow: hidden;
    box-shadow: 0 6px 18px rgba(0,0,0,0.18);
  }
  .card--back { top: 48px; }
  .card--front { top: 622px; }

  .gold-rule {
    position: absolute;
    left: 0; right: 0;
    height: 12px;
    background: repeating-linear-gradient(to bottom, var(--gold) 0 2px, var(--gold-light) 2px 3px, transparent 3px 5px);
  }
  .dark-field {
    position: absolute;
    left: 0; right: 0;
    background: radial-gradient(ellipse at 50% 35%, var(--black-soft), var(--black) 75%);
  }
  .pattern-band {
    position: absolute;
    left: 0; right: 0; bottom: 0;
    background: linear-gradient(to bottom, var(--band), var(--white));
  }

  /* front */
  .card--front .gold-rule.top { top: 0; }
  .card--front .dark-field { top: 12px; height: 318px; }
  .card--front .gold-rule.mid { top: 330px; }
  .card--front .pattern-band { top: 342px; }

  .brand {
    position: absolute;
    top: 92px; left: 0; right: 0;
    text-align: center;
    color: var(--gold);
  }
  .brand-name {
    font-weight: 700;
    font-size: 104px;
    line-height: 1;
    letter-spacing: 2px;
  }
  .brand-tagline {
    font-weight: 400;
    font-size: 30px;
    letter-spacing: 3px;
    margin-top: 8px;
  }

  /* back: contact side, no logo */
  .card--back .gold-rule.top { top: 0; }
  .card--back .dark-field { top: 12px; height: 370px; }
  .card--back .gold-rule.mid { top: 382px; }
  .card--back .pattern-band { top: 394px; }

  .identity {
    position: absolute;
    top: 96px; left: 0; right: 0;
    text-align: center;
  }
  .person-name {
    color: var(--text-light);
    font-weight: 700;
    font-size: 44px;
    line-height: 1.1;
  }
  .person-title {
    color: var(--gold);
    font-weight: 400;
    font-size: 22px;
    letter-spacing: 3px;
    text-transform: uppercase;
    margin-top: 12px;
  }

  .contact {
    position: absolute;
    bottom: 146px;
    color: var(--text-light);
    font-size: 17px;
    line-height: 34px;
  }
  .contact--left { left: 26px; }
  .contact--right { right: 26px; text-align: right; }
  .contact-row { display: flex; align-items: center; gap: 10px; }
  .contact--right .contact-row { justify-content: flex-end; }
  .contact-icon { width: 26px; height: 26px; flex: none; }
</style>
</head>
<body>

  <section class="card card--back" aria-label="Card back">
    <div class="gold-rule top"></div>
    <div class="dark-field" role="img" aria-label="Black damask patterned background"></div>
    <div class="gold-rule mid"></div>
    <div class="pattern-band" role="img" aria-label="White band with grey diamond pattern"></div>

    <div class="identity">
      <p class="person-name">Nora Vint</p>
      <p class="person-title">Principal Makeup Artist</p>
    </div>

    <div class="contact contact--left">
      <p class="contact-row">
        <svg class="contact-icon" viewBox="0 0 26 26" aria-hidden="true"><circle cx="13" cy="13" r="11.5" fill="none" stroke="#f1f1f1" stroke-width="1.5"/><path d="M9 7.5l2.2 2.6-1.3 1.5c.8 1.8 2.2 3.2 4 4l1.5-1.3 2.6 2.2-1.4 1.9c-4.3-.6-8.1-4.4-8.7-8.7z" fill="#f1f1f1"/></svg>
        0413 925 214
      </p>
      <p class="contact-row">
        <svg class="contact-icon" viewBox="0 0 26 26" aria-hidden="true"><g fill="none" stroke="#f1f1f1" stroke-width="1.3"><circle cx="13" cy="13" r="11.5"/><ellipse cx="13" cy="13" rx="4" ry="8"/><path d="M5 13h16M6.5 9h13M6.5 17h13M13 5v16"/></g></svg>
        www.lumirabeauty.com.au
      </p>
    </div>

    <div class="contact contact--right">
      <p class="contact-row">
        <span>22 Marlow Avenue<br>Brookfield NY 10452</span>
        <svg class="contact-icon" viewBox="0 0 26 26" aria-hidden="true"><circle cx="13" cy="13" r="11.5" fill="none" stroke="#f1f1f1" stroke-width="1.5"/><path d="M13 20s-5-5.2-5-9a5 5 0 0 1 10 0c0 3.8-5 9-5 9z" fill="none" stroke="#f1f1f1" stroke-width="1.4"/><circle cx="13" cy="11" r="1.8" fill="#f1f1f1"/></svg>
      </p>
      <p class="contact-row">
        nora@lumirabeauty.com.au
        <svg class="contact-icon" viewBox="0 0 26 26" aria-hidden="true"><circle cx="13" cy="13" r="11.5" fill="none" stroke="#f1f1f1" stroke-width="1.5"/><rect x="7" y="9" width="12" height="8.5" fill="none" stroke="#f1f1f1" stroke-width="1.3"/><path d="M7 9l6 5 6-5" fill="none" stroke="#f1f1f1" stroke-width="1.3"/></svg>
      </p>
    </div>
  </section>

  <section class="card card--front" aria-label="Card front">
    <div class="gold-rule top"></div>
    <div class="dark-field" role="img" aria-label="Black damask patterned background"></div>
    <div class="gold-rule mid"></div>
    <div class="pattern-band" role="img" aria-label="White band with grey diamond pattern"></div>

    <div class="brand">
      <p class="brand-name">Lumira</p>
      <p class="brand-tagline">MAKEUP ARTISTRY</p>
    </div>
  </section>

</body>
</html>
```